Meadowrun Honey labels

I have honey farm . I would like to sale it at grocery stores. I need really unique and very attractive designed labels, I would like to see writings 100% Natural honey and GMO free ,. Company name "MeadowrunHoney" . I want to put 2 labels and one ribbon tag in middle and round label on top of lid(only one diamond shape in the middle).I would like to see bee flying over red flower and at the left side flower field and right side bee putting honey into honey hives. I have attached example pictures of Honey Jars labels, tags and type. I have two different type of Honey jars i have also attached picture of those jars. For jar with red lid. If middle label little bit bigger than measurement thats ok because writing has to fit.

Target Market(s)

Grocery stores

Industry/Entity Type

Farm

Requirements
Must have
• 100% Natural Honey, GMO Free, Company name Meadowrun Honey, attractive and unique design. bee flying over flower, right side label flower field left side bee putting honey into bee hives.

```html
<!DOCTYPE html>
<html lang="en">
<head>
<meta charset="utf-8">
<title>Meadowrun Honey – Jar Label</title>
<link rel="stylesheet" href="https://fonts.googleapis.com/css2?family=Crimson+Pro:wght@500;600&display=swap">
<style>
  :root {
    --backdrop: #eef0f3;
    --label-black: #0d0b0a;
    --gold-deep: #a8812f;
    --gold-mid: #d8b665;
    --gold-light: #f6e6ae;
    --badge-red: #e2141b;
    --ink-white: #ffffff;
    --ink-dark: #1a140c;
  }
  html, body {
    margin: 0;
    padding: 0;
    width: 1198px;
    height: 1200px;
    overflow: hidden;
    background: var(--backdrop);
  }
  .label-canvas {
    display: block;
    width: 1198px;
    height: 1200px;
  }
  .badge-text {
    font-family: "Crimson Pro", Georgia, serif;
    font-weight: 600;
  }
  .brand-name {
    font-family: "Crimson Pro", Georgia, serif;
    font-weight: 500;
    fill: var(--gold-mid);
  }
</style>
</head>
<body>
<svg class="label-canvas" viewBox="0 0 1198 1200" xmlns="http://www.w3.org/2000/svg">
  <defs>
    <linearGradient id="goldSheen" x1="0" y1="0" x2="1" y2="0">
      <stop offset="0" stop-color="var(--gold-deep)"/>
      <stop offset="0.3" stop-color="var(--gold-light)"/>
      <stop offset="0.55" stop-color="var(--gold-mid)"/>
      <stop offset="0.8" stop-color="var(--gold-light)"/>
      <stop offset="1" stop-color="var(--gold-deep)"/>
    </linearGradient>
    <linearGradient id="goldVertical" x1="0" y1="0" x2="0" y2="1">
      <stop offset="0" stop-color="var(--gold-light)"/>
      <stop offset="1" stop-color="var(--gold-deep)"/>
    </linearGradient>
  </defs>

  <!-- ribbon band -->
  <g class="ribbon-band">
    <rect class="band-black" x="90" y="500" width="1018" height="200" fill="var(--label-black)"/>
    <path class="band-gold-edge" fill="url(#goldSheen)"
      d="M90 700 L90 655 L110 650 L130 646 L150 652 L175 644 L200 650 L225 642 L255 648 L285 640
         L315 646 L345 639 L380 647 L410 641 L440 648 L470 652 L470 700 Z
         M728 700 L728 652 L760 646 L790 650 L820 641 L850 648 L880 643 L910 649 L940 640
         L970 647 L1000 642 L1030 650 L1060 644 L1085 650 L1108 646 L1108 700 Z"/>
    <rect class="band-gold-line" x="90" y="598" width="1018" height="4" fill="url(#goldSheen)"/>
  </g>

  <!-- diamond badge -->
  <g class="diamond-badge">
    <polygon class="badge-gold-rim" points="599,412 760,600 599,788 438,600" fill="url(#goldVertical)"/>
    <polygon class="badge-black" points="599,420 752,600 599,780 446,600" fill="var(--label-black)"/>
    <polygon class="badge-white-line" points="599,440 735,600 599,760 463,600" fill="none" stroke="var(--ink-white)" stroke-width="2"/>
    <polygon class="badge-gold-line" points="599,450 726,600 599,750 472,600" fill="none" stroke="var(--gold-mid)" stroke-width="3"/>

    <polygon class="gmo-triangle" points="599,452 648,510 550,510" fill="var(--badge-red)"/>
    <text class="badge-text" x="599" y="503" text-anchor="middle" font-size="16" fill="var(--ink-white)">GMO Free</text>

    <!-- side connectors -->
    <polygon class="connector-left" points="449,600 461,588 473,600 461,612" fill="url(#goldVertical)"/>
    <polygon class="connector-right" points="725,600 737,588 749,600 737,612" fill="url(#goldVertical)"/>

    <!-- scroll ribbon -->
    <polygon class="scroll-tail-left" points="476,523 500,523 500,547 476,547 486,535" fill="var(--gold-deep)"/>
    <polygon class="scroll-tail-right" points="722,523 698,523 698,547 722,547 712,535" fill="var(--gold-deep)"/>
    <rect class="scroll-face" x="490" y="516" width="218" height="30" fill="url(#goldSheen)"/>
    <text class="badge-text" x="599" y="538" text-anchor="middle" font-size="17" fill="var(--ink-dark)">100% Natural Honey</text>

    <!-- company name -->
    <text class="brand-name" x="599" y="610" text-anchor="middle" font-size="40">Meadowrun</text>
    <text class="brand-name" x="599" y="652" text-anchor="middle" font-size="36">Honey</text>

    <!-- sprig ornament area -->
    <polygon class="sprig-ornament" role="img" aria-label="Gold botanical sprig ornament"
      points="599,676 636,716 599,744 562,716" fill="var(--gold-deep)" opacity="0.55"/>
  </g>
</svg>
</body>
</html>
```